Medical device box for kits used for self testing purposes. Attractive simplistic design

Looking for a design that will go on a box that offer multiple range of medical testing ranging from hormones panel to diabetes and thyroid hormones. looking for something attractive and simple to go on a box 6 x 4.5 x 1 inches. attached are some examples from competitors. and our logo that be incorporated with the design.
Picture of the boxes have been attached, pick the color you think goes best with your design.

Target Market(s)

Patients and regular consumers

Industry/Entity Type

Medical

Requirements
Nice to have
• Simple design that is eye catching

```html
<!DOCTYPE html>
<html lang="en">
<head>
<meta charset="utf-8">
<title>Thyroid Hormone Test – Box Front</title>
<link rel="stylesheet" href="https://fonts.googleapis.com/css2?family=Noto+Sans:wght@700;800&display=swap">
<style>
  :root {
    --navy: #0f1a3d;
    --sun: #ffe483;
    --sun-soft: #fff3c4;
    --paper: #ffffff;
    --edge: #6e6e6e;
  }
  html, body {
    margin: 0;
    padding: 0;
    width: 1200px;
    height: 898px;
    overflow: hidden;
    background: var(--paper);
  }
  .box-front {
    position: relative;
    width: 1200px;
    height: 898px;
    box-sizing: border-box;
    border: 2px solid var(--edge);
    background: var(--paper);
    overflow: hidden;
    font-family: "Noto Sans", "DejaVu Sans", sans-serif;
  }
  .brand {
    position: absolute;
    left: 67px;
    top: 78px;
    display: flex;
    align-items: center;
    gap: 12px;
    color: var(--navy);
    font-weight: 800;
    font-size: 64px;
    line-height: 1;
    letter-spacing: 0;
  }
  .brand-dot {
    width: 42px;
    height: 42px;
    border-radius: 50%;
    background: var(--sun);
  }
  .dot-field {
    position: absolute;
    left: 918px;
    top: 0;
    width: 282px;
    height: 898px;
    background: linear-gradient(90deg, var(--paper) 0%, var(--sun-soft) 100%);
  }
  .title-band {
    position: absolute;
    left: 0;
    top: 0;
    width: 1200px;
    height: 898px;
  }
  .title-band path, .title-band rect { fill: var(--sun); }
  .product-name {
    position: absolute;
    left: 58px;
    top: 657px;
    margin: 0;
    color: var(--navy);
    font-weight: 700;
    font-size: 64px;
    line-height: 68px;
    letter-spacing: 4px;
  }
</style>
</head>
<body>
  <main class="box-front">
    <div class="dot-field" role="img" aria-label="Decorative pattern of pale yellow dots growing larger toward the right edge"></div>

    <svg class="title-band" viewBox="0 0 1200 898" aria-hidden="true">
      <path d="M0 640 H627 C760 640 873 710 873 810 H0 Z"/>
      <rect x="1137" y="640" width="63" height="170"/>
    </svg>

    <div class="brand">
      <span class="brand-dot"></span>
      <span class="brand-name">Kovelin</span>
    </div>

    <h1 class="product-name">Thyroid<br>Hormone Test</h1>
  </main>
</body>
</html>
```